BrambleWorks business card

Looking for business card design that supports our company/software values. We have 2 logo designs at the moment but open to change if you think you can enhance the brand. Check out website www.brambleworks.com.au.

Target Market(s)

Education

Contact Information for Business Card

Name, title, mobile, email and website

Font styles to use
Sans Serif

Colors

Designer to choose colors to be used in the design.

Requirements
Must have
• BrambleWorks logo with tree and tagline on rear side with dark grey background colour

```html
<!DOCTYPE html>
<html lang="en">
<head>
<meta charset="utf-8">
<title>BrambleWorks Business Card</title>
<link rel="stylesheet" href="https://fonts.googleapis.com/css2?family=Montserrat:wght@700&family=Ubuntu:wght@400;500&display=swap">
<style>
  :root {
    --page-bg: #d9dadb;
    --card-dark: #4a4b48;
    --card-light: #ffffff;
    --ink: #3f403e;
    --ink-soft: #555653;
    --leaf-green: #3c7a2a;
    --accent-gold: #f0a81c;
    --rule: #6b6c69;
  }
  * { margin: 0; padding: 0; box-sizing: border-box; }
  html, body { width: 1200px; height: 800px; overflow: hidden; }
  body {
    background: var(--page-bg);
    font-family: "Ubuntu", sans-serif;
    position: relative;
  }
  .card {
    position: absolute;
    width: 560px;
    height: 320px;
    border-radius: 2px;
    box-shadow: 0 6px 18px rgba(0,0,0,0.18);
    overflow: hidden;
  }
  /* Rear side */
  .card--rear {
    left: 380px;
    top: 50px;
    background: var(--card-dark);
  }
  .rear-pattern {
    position: absolute;
    inset: 0;
    background: linear-gradient(135deg, #4f504d 0%, #474845 100%);
  }
  .rear-url {
    position: absolute;
    left: 34px;
    bottom: 36px;
    color: #f2f2f2;
    font-size: 12px;
    letter-spacing: 2.4px;
  }
  .rear-mark {
    position: absolute;
    right: 30px;
    bottom: 28px;
    display: flex;
    align-items: center;
    gap: 6px;
    color: #ffffff;
    font-size: 13px;
    font-weight: 500;
  }
  .rear-mark__dot {
    width: 10px; height: 10px;
    border-radius: 50%;
    background: var(--accent-gold);
  }
  /* Front side */
  .card--front {
    left: 260px;
    top: 420px;
    background: var(--card-light);
  }
  .brand {
    position: absolute;
    left: 150px;
    top: 50px;
    width: 290px;
  }
  .brand__row { display: flex; align-items: center; gap: 12px; }
  .brand__dot {
    width: 14px; height: 14px;
    border-radius: 50%;
    background: var(--leaf-green);
    flex: none;
  }
  .brand__name {
    font-size: 42px;
    font-weight: 500;
    color: var(--ink);
    letter-spacing: 0.5px;
    line-height: 1;
  }
  .brand__rule {
    height: 1px;
    background: var(--rule);
    margin: 8px 0 6px;
  }
  .brand__tagline {
    font-size: 17px;
    color: var(--ink-soft);
    letter-spacing: 0.6px;
    text-align: right;
  }
  .person {
    position: absolute;
    right: 302px;
    top: 196px;
    text-align: right;
  }
  .person__name {
    font-family: "Montserrat", sans-serif;
    font-weight: 700;
    font-size: 18px;
    color: var(--leaf-green);
  }
  .person__title {
    font-size: 15px;
    color: var(--ink-soft);
    margin-top: 2px;
  }
  .divider {
    position: absolute;
    left: 278px;
    top: 186px;
    width: 6px;
    height: 72px;
  }
  .contact {
    position: absolute;
    left: 298px;
    top: 192px;
    list-style: none;
    font-size: 15px;
    color: var(--ink);
    line-height: 21px;
  }
  .contact li { display: flex; align-items: center; gap: 7px; }
  .contact svg { width: 13px; height: 13px; flex: none; }
</style>
</head>
<body>

  <section class="card card--rear" aria-label="Business card rear side">
    <div class="rear-pattern" role="img" aria-label="Faint repeating brand pattern across the dark grey background"></div>
    <p class="rear-url">www.brambleworks.com.au</p>
    <div class="rear-mark"><span class="rear-mark__dot"></span>BrambleWorks</div>
  </section>

  <section class="card card--front" aria-label="Business card front side">
    <div class="brand">
      <div class="brand__row">
        <span class="brand__dot"></span>
        <span class="brand__name">BrambleWorks</span>
      </div>
      <div class="brand__rule"></div>
      <p class="brand__tagline">Student Success Platform</p>
    </div>

    <div class="person">
      <p class="person__name">Daniel Hartley</p>
      <p class="person__title">President</p>
    </div>

    <svg class="divider" viewBox="0 0 6 72" aria-hidden="true">
      <line x1="3" y1="3" x2="3" y2="69" stroke="#555653" stroke-width="1"/>
      <circle cx="3" cy="3" r="2.5" fill="#555653"/>
      <circle cx="3" cy="69" r="2.5" fill="#555653"/>
    </svg>

    <ul class="contact">
      <li>
        <svg viewBox="0 0 13 13" aria-hidden="true"><rect x="3.5" y="0.8" width="6" height="11.4" rx="1" fill="none" stroke="#3c7a2a" stroke-width="1.2"/><line x1="5.5" y1="10.3" x2="7.5" y2="10.3" stroke="#3c7a2a"/></svg>
        +61 400 555 218
      </li>
      <li>
        <svg viewBox="0 0 13 13" aria-hidden="true"><rect x="0.8" y="2.5" width="11.4" height="8" fill="none" stroke="#3c7a2a" stroke-width="1.2"/><polyline points="0.8,2.5 6.5,7 12.2,2.5" fill="none" stroke="#3c7a2a" stroke-width="1.2"/></svg>
        daniel@brambleworks.com.au
      </li>
      <li>
        <svg viewBox="0 0 13 13" aria-hidden="true"><circle cx="6.5" cy="6.5" r="5.6" fill="none" stroke="#3c7a2a" stroke-width="1.1"/><ellipse cx="6.5" cy="6.5" rx="2.4" ry="5.6" fill="none" stroke="#3c7a2a" stroke-width="1"/><line x1="0.9" y1="6.5" x2="12.1" y2="6.5" stroke="#3c7a2a"/></svg>
        www.brambleworks.com.au
      </li>
    </ul>
  </section>

</body>
</html>
```